Label for flatbread

create an innovative and visually appealing label for flatbread packaging. The goal is to blend traditional bread-making heritage with a modern aesthetic that attracts consumers in retail environments while communicating freshness, quality, and authenticity.

To design a front-facing package label for flatbread that:
• Captures the essence of artisanal baking and cultural tradition.
• Stands out on shelves with strong visual appeal.
• You can use folk art to create the images on the label, elements like flatbread, wheat,
We want to print the label in a sticker and put it on bread bag, so consider that you are designing a label in a frame for instance 4 inch in 5 inch rectangular. We would like that the label has theme like the uploaded images (does not need to be similar to the uploaded images) these images give you a clue .

Target Market(s)

Groceries stores in Vancouver area Canada

Industry/Entity Type

Bakery

Font styles to use
Other font styles liked:
• feel free to choose your font yourself

Requirements
Must have
• Design the label to attract consumers and encourage them to choose this bread. Create an eye-catching label that entices consumers to try this bread. Make the label so appealing that consumers can’t resist picking up this bread.
Nice to have
• Clean, Illustration or icon of flatbread, Subtle grain (whole wheat!) or flour textures in the background to suggest craftsmanship, Made in Canada
Should not have
• we do not limit artists, use your imagination, do not put bread picture, the bread picture must be hand drawn

```html
<!DOCTYPE html>
<html lang="en">
<head>
<meta charset="utf-8">
<title>Flatbreads Original Label</title>
<link href="https://fonts.googleapis.com/css2?family=Bebas+Neue&family=Alfa+Slab+One&family=Roboto+Slab:wght@400;700&display=swap" rel="stylesheet">
<style>
  :root {
    --canvas: #dcdcdc;
    --label-black: #121212;
    --gold: #f0aa12;
    --white: #ffffff;
    --ink: #111111;
    --crust: #c98a3a;
    --crumb: #e8c27a;
  }
  * { box-sizing: border-box; margin: 0; padding: 0; }
  html, body { width: 1200px; height: 847px; overflow: hidden; }
  body { background: var(--canvas); position: relative; }

  .label {
    position: absolute; left: 330px; top: 34px;
    width: 540px; height: 778px;
    background: radial-gradient(ellipse at 50% 40%, #1e1e1e, var(--label-black) 70%);
    overflow: hidden;
  }
  .label__frame {
    position: absolute; left: 22px; top: 20px; right: 22px; bottom: -10px;
    border: 1.5px solid var(--white);
  }
  .gold-band { position: absolute; left: 189px; width: 163px; background: var(--gold); }
  .gold-band--top { top: 23px; height: 132px; }
  .gold-band--top::after {
    content: ""; position: absolute; left: 0; right: 0; bottom: -3px; height: 3px;
    background: conic-gradient(from -45deg at bottom, var(--gold) 90deg, transparent 0) 50% / 6px 100%;
  }
  .gold-band--bottom { top: 495px; height: 80px; }
  .gold-band--bottom::before {
    content: ""; position: absolute; left: 0; right: 0; top: -3px; height: 3px;
    background: conic-gradient(from 135deg at top, var(--gold) 90deg, transparent 0) 50% / 6px 100%;
  }
  .net-weight {
    position: absolute; left: 0; right: 0; top: 22px; text-align: center;
    font: 700 11px "Roboto Slab", serif; color: var(--ink); letter-spacing: 0.5px;
  }

  .product-name {
    position: absolute; left: 0; right: 0; top: 160px; text-align: center;
    font: 400 101px/1 "Bebas Neue", sans-serif; color: var(--white); letter-spacing: 3px;
  }
  .variant {
    position: absolute; left: 97px; top: 255px; width: 346px; height: 41px;
    background: var(--gold); border-radius: 7px 7px 0 0;
    text-align: center;
    font: 400 31px/41px "Alfa Slab One", serif; color: var(--ink); letter-spacing: 6px;
  }
  .tagline {
    position: absolute; left: 97px; top: 296px; width: 346px; height: 40px;
    background: var(--white); border-radius: 0 0 7px 7px;
    padding-top: 6px; text-align: center;
    font: 400 9.3px/13px "Roboto Slab", serif; color: var(--ink);
  }
  .claims {
    position: absolute; left: 0; right: 0; top: 347px; text-align: center;
    font: 400 8.4px/10.3px "Roboto Slab", serif; color: var(--white);
  }

  .badges { position: absolute; left: 0; right: 0; top: 389px; display: flex; justify-content: center; gap: 24px; }
  .badge { width: 36px; text-align: center; }
  .badge__tab {
    width: 36px; height: 42px; background: var(--white);
    border-radius: 18px 18px 3px 3px;
    display: flex; align-items: center; justify-content: center;
    padding-bottom: 8px;
  }
  .badge__tab svg { width: 18px; height: 18px; }
  .badge__text {
    margin-top: -10px; font: 700 6.6px/8px "Roboto Slab", serif; color: var(--white);
    position: relative;
  }
  .badge__text span { color: var(--ink); }
  .badge__caption { display: block; background: var(--white); border-radius: 0 0 3px 3px; padding-bottom: 3px; color: var(--ink); }

  .bread-art {
    position: absolute; left: 37px; top: 530px; width: 470px; height: 470px;
    border-radius: 50%;
    background: radial-gradient(circle at 50% 45%, var(--crumb), #d9a658 62%, var(--crust) 92%, #8a5a25);
  }
  .grain-art {
    position: absolute; left: 40px; top: 535px; width: 60px; height: 120px;
    border-radius: 40%;
    background: radial-gradient(ellipse, #d8a860, rgba(216,168,96,0) 70%);
  }

  .pack-badge {
    position: absolute; left: 378px; top: 526px; width: 112px; height: 112px;
    border-radius: 50%; background: #0c0c0c;
    display: flex; align-items: center; justify-content: center;
  }
  .pack-badge__ring {
    width: 96px; height: 96px; border-radius: 50%; border: 2px solid var(--gold);
    text-align: center; color: var(--gold);
  }
  .pack-badge__count { display: block; font: 400 44px/1 "Alfa Slab One", serif; margin-top: 8px; }
  .pack-badge__unit { display: block; font: 400 17px/1 "Alfa Slab One", serif; margin-top: -3px; }
</style>
</head>
<body>
  <main class="label">
    <div class="label__frame"></div>

    <div class="gold-band gold-band--top"></div>

    <h1 class="product-name">FLATBREADS</h1>
    <div class="variant">ORIGINAL</div>
    <p class="tagline">LOREM IPSUM DOLOR SIT AMET, CONSECTETUR ADIPISCING<br>ELIT, SED DO EIUSMOD TEMPOR INCIDIDUNT</p>

    <p class="claims">NO ARTIFICIAL PRESERVATIVES<br>AUTHENTIC TASTE<br>OVEN BAKED</p>

    <ul class="badges" style="list-style:none">
      <li class="badge">
        <div class="badge__tab">
          <svg viewBox="0 0 20 20"><path d="M4 4 L10 17 L14 6" fill="none" stroke="#111" stroke-width="1.8"/><path d="M14 6 C15 3 17 2 18 2 C18 4 16 6 14 6Z" fill="#111"/></svg>
        </div>
        <span class="badge__caption badge__text">100%<br>VEGAN</span>
      </li>
      <li class="badge">
        <div class="badge__tab">
          <svg viewBox="0 0 20 20" fill="#111"><ellipse cx="10" cy="4" rx="2.4" ry="3"/><ellipse cx="6" cy="9" rx="2.6" ry="3"/><ellipse cx="14" cy="9" rx="2.6" ry="3"/><ellipse cx="7" cy="15.5" rx="2.6" ry="3"/><ellipse cx="13" cy="15.5" rx="2.6" ry="3"/></svg>
        </div>
        <span class="badge__caption badge__text">WHEAT<br>BASED</span>
      </li>
      <li class="badge">
        <div class="badge__tab">
          <svg viewBox="0 0 20 20" fill="#111"><rect x="5" y="4" width="2.4" height="9" rx="1.2"/><rect x="8" y="1.5" width="2.4" height="11" rx="1.2"/><rect x="11" y="2.5" width="2.4" height="10" rx="1.2"/><rect x="14" y="5" width="2.2" height="8" rx="1.1"/><path d="M5 11 H16 V15 C16 18 13 19.5 10.5 19.5 C7 19.5 5 17 3 13 L1.8 10.5 C2.8 9.6 4 10 5 11Z"/></svg>
        </div>
        <span class="badge__caption badge__text">HAND<br>MADE</span>
      </li>
      <li class="badge">
        <div class="badge__tab">
          <svg viewBox="0 0 20 20" fill="#111"><path d="M10 19 V10" stroke="#111" stroke-width="1.6"/><path d="M10 12 C6 12 3 9 3 5 C7 5 10 8 10 12Z"/><path d="M10 11 C10 7 13 4 17 4 C17 8 14 11 10 11Z"/><circle cx="4" cy="2" r="1"/><circle cx="15" cy="1.5" r="0.9"/></svg>
        </div>
        <span class="badge__caption badge__text">FRESH<br>PRODUCE</span>
      </li>
    </ul>

    <div class="gold-band gold-band--bottom">
      <p class="net-weight">NET WT. 12OZ</p>
    </div>

    <div class="bread-art" role="img" aria-label="Hand-drawn golden baked flatbread with toasted brown spots"></div>
    <div class="grain-art" role="img" aria-label="Scattered wheat grains"></div>

    <div class="pack-badge">
      <div class="pack-badge__ring">
        <span class="pack-badge__count">6</span>
        <span class="pack-badge__unit">PACK</span>
      </div>
    </div>
  </main>
</body>
</html>
```